Vigorhaven home exercise studio needs a brochure design

My problem is that I have had a fitness studio within my home for 3 years and only 2 clients per week to show for it! I need a fitness brochure designed that will literally want to make a customer pick up the phone and book a training session!

If there is any way possible to convince those exercise lovers or those who wish to become active and healthy who want to train in a private home exercise studio setting than I will be very content and happy. Obviosuly my studio within my home is not exposed to the general public and I understand that this is the reason for a shortage of clients.

I have an exercise studio with my home. It is literally the size of 6-7 x area of a standard bedroom. Most importantly, it contains the latest state of the art exercise equipment (treamills, rowers, cycle & recumberant bikes, elastic cords, bands, medballs, resistance machines, cables, squat racks, you name it..

In addition, compared to many other personal trainers out within the industry, I have clearly distinguished myself from the rest in a positive way. Firstly, I have had an extensive background as an elite athlete (NSW wrestling representitive), secondly I have acquired a solid foundation of exercise science principles through 4 years of university studies (compared to most other trainers out there). Because my studio is private and obviously lacks many elements that a typical gym setting such as peak motion, then we must be able to highlight the positives that arise from my studio compared to peak motion or any other franchise (eg: no cancellation pollicies, no signing up for contracts, no membership fees). in addition, we must hihglight the fact that a private studio like mine will attract those who prefer not to train around others they do not know as there is no sharing of exercise equipment or duration of time one must be on a certain exercise.

We all know someone who prefers not to train in a typical gym setting where people have to compete against others for the equipment yet alone deal with the amount of starring and chatter that goes on. In addition it can get intimidating for those who prefer not many people around them. My studio is designed for any age or fitness category. In addition group training is avaliable.
In addition, I am flexible and sometimes permit going overtime for those clients who were late for there appointment. Clients that come to my home to exercise feel as if they are training within there own home rather than feeling the intimidation of going into a gym setting such as peak motion.

If we can highlight all that has been mentioned within my brochure than thats great!

Target Market(s)

I design exercise programs and train all age groups and fitness levels

Industry/Entity Type

University

Requirements
Must have
• There must be a quote in the brochure that mentions "Together,the sky is our limit"

Must have "vigorhaven" logo

must have testimonials:

Colin -"My golf drive has increased dramatically from the use of sports specific exercises that Howard was able to deliver. The pain in my lower back has now ceased to flare up after a game"

Miriam - "Howard's knowledge and application of exercise science and health has helped me achieve a stronger and leaner body in addition to improving my 5km walking time"

Must have my qualifications:
Certificate 4 personal trainer
Diploma of fitness
Bachelor of exercise and sport science
Diploma of remedial massage
First Aid certificate

Must state that I am registered with Active Registry Australia

Must have that I Specialize in:

1. exercise rehabilitation
2. sport specific conditioning
3. Functional strength
4. Fat loss and toning
5. Core strength & stability
6. Flexibility
7. Cardio-respiratory fitness

Must have my mobile number: 0427 586 903
Must have my email adress: hwtrelford@quillmail.com.au
Nice to have
• any background images that represent motivation, will and determination.

```html
<!DOCTYPE html>
<html lang="en">
<head>
<meta charset="utf-8">
<title>Vigorhaven Brochure Cover</title>
<link rel="stylesheet" href="https://fonts.googleapis.com/css2?family=Anton&family=Arimo:wght@700&family=PT+Sans:wght@400;700&family=Tinos:wght@700&display=swap">
<style>
  :root {
    --haze: #e3ecf5;
    --sky-mid: #a9c3de;
    --valley: #5f86b4;
    --valley-deep: #4d77a8;
    --rock-light: #d3dbe4;
    --rock: #aebccb;
    --quote-navy: #2d3b8e;
    --headline-magenta: #b1408e;
    --headline-navy: #2c3f8f;
    --headline-white: #ffffff;
    --headline-shade: #7c8591;
    --brand-red: #d9252b;
    --contact-navy: #2a2f7c;
    --cloud-white: #ffffff;
    --no-green: #2e7d32;
    --no-red: #c62828;
    --no-blue: #1f5fae;
  }
  * { margin: 0; padding: 0; box-sizing: border-box; }
  html, body { width: 1200px; height: 839px; overflow: hidden; background: #fff; }
  .spread { position: relative; width: 1200px; height: 839px; overflow: hidden; }
  .backdrop-photo {
    position: absolute; inset: 0;
    background:
      radial-gradient(ellipse 330px 260px at 170px 720px, var(--rock-light) 0%, rgba(211,219,228,.85) 55%, rgba(211,219,228,0) 100%),
      radial-gradient(ellipse 230px 280px at 1090px 700px, var(--rock-light) 0%, rgba(211,219,228,.8) 55%, rgba(211,219,228,0) 100%),
      radial-gradient(ellipse 700px 200px at 500px 380px, var(--valley-deep) 0%, rgba(77,119,168,0) 100%),
      linear-gradient(180deg, var(--haze) 0%, var(--sky-mid) 25%, var(--valley) 50%, var(--valley) 62%, var(--rock) 100%);
  }
  .quote {
    position: absolute; left: 640px; top: 48px; width: 500px; text-align: center;
    font-family: "Tinos", "Times New Roman", serif; font-weight: 700; font-size: 25px;
    color: var(--quote-navy);
  }
  .headline {
    position: absolute; left: 678px; width: 400px; text-align: center;
    font-family: "Anton", "Arial Narrow", sans-serif;
  }
  .headline span { display: block; }
  .good-news {
    top: 96px; font-size: 66px; line-height: 76px; color: var(--headline-magenta);
    -webkit-text-stroke: 1.5px #fff; letter-spacing: .5px;
    text-shadow: 2px 2px 3px rgba(0,0,0,.25);
  }
  .white-words {
    color: var(--headline-white); font-size: 55px; line-height: 48px; letter-spacing: 1px;
    -webkit-text-stroke: 1px var(--headline-shade);
    text-shadow: 2px 2px 2px rgba(60,70,80,.45);
  }
  .lovers-block { top: 166px; }
  .start-block {
    top: 334px; font-size: 58px; line-height: 48px; color: var(--headline-navy);
    -webkit-text-stroke: 1px #fff; letter-spacing: .5px;
    text-shadow: 2px 2px 3px rgba(0,0,0,.25);
  }
  .home-block { top: 432px; }
  .cloud { position: absolute; }
  .cloud svg { position: absolute; inset: 0; }
  .cloud-text {
    position: relative; display: flex; flex-direction: column; align-items: center; justify-content: center;
    height: 100%; font-family: "PT Sans", "Myriad Pro", sans-serif; font-size: 15px; line-height: 17px; text-align: center;
  }
  .cloud-text strong { font-weight: 700; font-size: 15px; }
  .cloud-contracts { left: 630px; top: 268px; width: 150px; height: 68px; color: var(--no-green); }
  .cloud-cancel { left: 990px; top: 190px; width: 152px; height: 72px; color: var(--no-red); }
  .cloud-fees { left: 660px; top: 487px; width: 124px; height: 68px; color: var(--no-blue); }
  .brand {
    position: absolute; font-family: "Anton", "Arial Narrow", sans-serif; color: var(--brand-red);
    letter-spacing: .5px;
  }
  .brand-back { left: 188px; top: 704px; width: 184px; text-align: center; font-size: 38px; }
  .brand-front { left: 1036px; top: 752px; width: 140px; text-align: center; font-size: 30px; }
  .contact {
    position: absolute; left: 130px; top: 772px; width: 320px; text-align: center;
    font-family: "Arimo", Arial, sans-serif; font-weight: 700; font-size: 13px; line-height: 18px;
    color: var(--contact-navy);
  }
</style>
</head>
<body>
<main class="spread">
  <div class="backdrop-photo" role="img" aria-label="Photograph: a hiker seen from behind raising a fist on a granite cliff ledge at right, above a hazy blue forested mountain valley with a pale granite dome at lower left"></div>

  <p class="quote">"Together, the sky is our limit"</p>

  <h1 class="headline good-news">GOOD NEWS</h1>
  <p class="headline white-words lovers-block"><span>for</span><span>exercise</span><span>lovers</span></p>
  <h2 class="headline start-block"><span>START</span><span>EXERCISE</span></h2>
  <p class="headline white-words home-block"><span>within</span><span>your</span><span>own</span><span>home</span><span>atmosphere</span></p>

  <div class="cloud cloud-contracts">
    <svg viewBox="0 0 150 68" width="150" height="68"><path d="M22 58c-14 0-19-14-9-20-6-12 8-22 19-16 4-14 24-18 34-8 8-10 28-8 32 4 14-4 28 6 24 18 12 4 10 22-4 22z" fill="var(--cloud-white)" stroke="#c9d3dc" stroke-width="1.5"/></svg>
    <div class="cloud-text"><strong>NO</strong><span>Signing up</span><span>for contracts</span></div>
  </div>
  <div class="cloud cloud-cancel">
    <svg viewBox="0 0 152 72" width="152" height="72"><path d="M22 62c-14 0-19-14-9-21-6-12 8-23 19-17 4-14 24-19 35-8 8-11 29-9 33 4 14-4 29 6 25 19 12 4 10 23-4 23z" fill="var(--cloud-white)" stroke="#c9d3dc" stroke-width="1.5"/></svg>
    <div class="cloud-text"><strong>NO</strong><span>Cancellation</span><span>Pollicies</span></div>
  </div>
  <div class="cloud cloud-fees">
    <svg viewBox="0 0 124 68" width="124" height="68"><path d="M18 58c-12 0-16-14-7-20-5-12 7-22 16-16 3-14 20-18 28-8 7-10 23-8 27 4 12-4 23 6 20 18 10 4 8 22-3 22z" fill="var(--cloud-white)" stroke="#c9d3dc" stroke-width="1.5"/></svg>
    <div class="cloud-text"><strong>NO</strong><span>Membership</span><span>fees</span></div>
  </div>

  <p class="brand brand-back">Vigorhaven</p>
  <p class="contact">mobile : 0427 586 903<br>email: hwtrelford@quillmail.com.au</p>

  <p class="brand brand-front">Vigorhaven</p>
</main>
</body>
</html>
```